The Morrow Ledgers Website

I need a website to help promote the series of science fiction novels that I am in the process of writing.

I have some content and photos and am in the process of getting some new book cover artwork designed.

I have a current website/domain etc http://www.vantorpagehouse.co.nz but I need something a little more professional and eye catchig but I also want to be able to manage the content myself.

I can send e-versions of the two completed novels for context to any takers

```html
<!DOCTYPE html>
<html lang="en">
<head>
<meta charset="utf-8">
<title>The Morrow Ledgers</title>
<link rel="stylesheet" href="https://fonts.googleapis.com/css2?family=Open+Sans:ital,wght@0,400;0,600;1,400&display=swap">
<style>
  :root {
    --brand-blue: #0a6cbf;
    --link-blue: #0b6fc4;
    --nav-black: #0d0d0d;
    --body-text: #555;
    --page-bg: #ffffff;
    --panel-bg: #f4f4f4;
    --panel-border: #dcdcdc;
    --footer-bg: #333333;
    --footer-text: #cfcfcf;
    --button-grey: #6b6b6b;
  }
  * { box-sizing: border-box; margin: 0; padding: 0; }
  html, body { width: 1150px; height: 1200px; overflow: hidden; }
  body { font-family: "Open Sans", Arial, sans-serif; background: var(--page-bg); position: relative; color: var(--body-text); }

  .site-header { position: absolute; left: 0; top: 0; width: 1150px; height: 75px; background: var(--brand-blue); }
  .site-title { position: absolute; left: 96px; top: 12px; font-size: 37px; font-weight: 400; color: #fff; letter-spacing: .3px; }
  .social-square { position: absolute; top: 22px; width: 31px; height: 31px; background: #fff; border-radius: 3px; }
  .social-square.first { left: 810px; }
  .social-square.second { left: 858px; }
  .search-box { position: absolute; left: 905px; top: 22px; width: 150px; height: 31px; background: #fff; border-radius: 3px; }
  .search-box span { position: absolute; left: 13px; top: 7px; font-size: 13px; color: #999; }
  .search-box .divider { position: absolute; left: 119px; top: 5px; width: 1px; height: 21px; background: #ccc; }
  .search-box svg { position: absolute; left: 125px; top: 5px; }

  .main-nav { position: absolute; left: 0; top: 76px; width: 1150px; height: 49px; background: linear-gradient(#2a2a2a, var(--nav-black)); border-top: 1px solid #3a3a3a; }
  .main-nav a { position: absolute; top: 15px; font-size: 15px; color: #bbb; text-decoration: none; letter-spacing: .3px; }
  .main-nav a.current { color: #fff; }

  .hero { position: absolute; left: 0; top: 125px; width: 1150px; height: 472px;
    background: linear-gradient(160deg, #8b7f74 0%, #4a4b5a 30%, #2c3550 55%, #5d3a36 75%, #9a9aa0 100%); }
  .hero-arrow { position: absolute; top: 219px; width: 32px; height: 32px; border-radius: 50%; background: rgba(235,235,235,.85); }
  .hero-arrow.prev { left: 97px; }
  .hero-arrow.next { left: 1022px; }
  .hero-arrow svg { position: absolute; left: 10px; top: 9px; }
  .hero-caption { position: absolute; left: 125px; top: 416px; height: 38px; padding: 0 13px; background: rgba(0,0,0,.72); color: #fff; font-size: 21px; line-height: 38px; }

  .intro { position: absolute; left: 98px; top: 624px; width: 705px; }
  .section-title { font-size: 23px; font-weight: 400; color: var(--link-blue); }
  .intro p { font-size: 13px; line-height: 22px; margin-top: 8px; }
  .intro .section-title + p { margin-top: 12px; }
  .read-more { display: inline-block; margin-top: 19px; width: 92px; height: 33px; line-height: 33px; text-align: center; border-radius: 3px; background: linear-gradient(#8a8a8a, var(--button-grey)); color: #fff; font-size: 13px; }

  .rule { position: absolute; left: 96px; top: 930px; width: 711px; height: 1px; background: #d8d8d8; }
  .reviews-title { position: absolute; left: 98px; top: 948px; font-size: 19px; color: var(--link-blue); font-weight: 400; }
  .reviews-next { position: absolute; left: 780px; top: 953px; }
  .review-card { position: absolute; left: 99px; top: 982px; width: 698px; height: 98px; background: #f0f0f0; border-radius: 3px; padding: 14px 25px; }
  .review-card blockquote { font-style: italic; font-size: 15px; line-height: 22px; color: #777; }
  .review-card cite { display: block; margin-top: 4px; font-style: normal; font-size: 15px; color: #222; }

  .sidebar { position: absolute; left: 823px; top: 597px; width: 232px; height: 484px; background: linear-gradient(90deg, #f0f0f0, #fbfbfb); border: 1px solid var(--panel-border); border-top: none; }
  .sidebar h2 { position: absolute; left: 22px; top: 32px; font-size: 19px; font-weight: 400; color: var(--link-blue); }
  .book { position: absolute; left: 22px; width: 210px; }
  .book .cover { position: absolute; left: 0; top: 0; width: 101px; height: 149px; }
  .book h3 { position: absolute; left: 112px; top: -4px; width: 96px; font-size: 17px; line-height: 21px; font-weight: 400; color: var(--link-blue); }
  .book p { position: absolute; left: 112px; font-size: 12px; line-height: 17px; color: #222; }
  .book.latest { top: 687px; }
  .book.latest .cover { background: linear-gradient(#c0181c 0 8%, #1a1a1a 30%, #9a9a9a 55%, #111 70%, #e01b22 72%); }
  .book.first { top: 887px; }
  .book.first .cover { background: linear-gradient(#111 0%, #8a8f96 35%, #b8bbc0 55%, #3a3a3c 72%, #f5f5f2 74%, #f5f5f2 97%, #111 100%); }

  .site-footer { position: absolute; left: 0; top: 1102px; width: 1150px; height: 98px; background: var(--footer-bg); }
  .footer-links { position: absolute; left: 97px; top: 22px; font-size: 12.5px; color: var(--footer-text); word-spacing: 0; }
  .footer-links span { margin: 0 10px; }
  .footer-links span.sep { color: #aaa; margin: 0; }
  .footer-links a:first-child { margin-left: 0; }
  .footer-links a { color: var(--footer-text); text-decoration: none; margin: 0 12px; }
  .copyright { position: absolute; left: 97px; top: 57px; font-size: 12.5px; color: var(--footer-text); }
  .footer-social { position: absolute; top: 36px; width: 25px; height: 25px; border-radius: 50%; background: #666; }
</style>
</head>
<body>

<header class="site-header">
  <div class="site-title">The Morrow Ledgers</div>
  <div class="social-square first" aria-hidden="true"></div>
  <div class="social-square second" aria-hidden="true"></div>
  <div class="search-box">
    <span>Search</span>
    <div class="divider"></div>
    <svg width="20" height="20" viewBox="0 0 20 20"><circle cx="8" cy="8" r="6" fill="none" stroke="#999" stroke-width="2"/><line x1="12.5" y1="12.5" x2="18" y2="18" stroke="#999" stroke-width="3" stroke-linecap="round"/></svg>
  </div>
</header>

<nav class="main-nav">
  <a class="current" style="left:141px">HOME</a>
  <a style="left:272px">REVIEWS</a>
  <a style="left:420px">ABOUT</a>
  <a style="left:557px">BLOG</a>
  <a style="left:684px">CONTACT</a>
  <a style="left:839px">NEWS</a>
  <a style="left:967px">LINKS</a>
</nav>

<section class="hero" role="img" aria-label="Photograph of a table display of stacked science fiction paperbacks with colourful covers">
  <div class="hero-arrow prev"><svg width="12" height="14" viewBox="0 0 12 14"><polyline points="8,1 2,7 8,13" fill="none" stroke="#999" stroke-width="1.5"/></svg></div>
  <div class="hero-arrow next"><svg width="12" height="14" viewBox="0 0 12 14"><polyline points="4,1 10,7 4,13" fill="none" stroke="#999" stroke-width="1.5"/></svg></div>
  <div class="hero-caption">The Morrow Ledgers come to Arlen's scifi page where you can find links to his scifi novels</div>
</section>

<main class="intro">
  <h1 class="section-title">Welcome to The Morrow Ledgers</h1>
  <p>The Second Tide is the second novel in the Morrow Ledgers series and follows on from the first novel where our unlikely protagonists were kidnapped by a desperate food research team from the Planet Morrow. The researchers were on a mission to locate expertise to assist them in developing organic food sources to feed their people as their planet's synthetic food production systems had begun to fail for some inexplicable reason.</p>
  <p>The Morrow team had selected a team of experts at random without really understanding the expertise that they required to achieve their objectives. However, more by good luck than good management, they stumbled on some-one who could generate new food production systems in the form of New Zild style grasslands based cattle farm, station or ranch.</p>
  <span class="read-more">Read more</span>
</main>

<div class="rule"></div>
<h2 class="reviews-title">Reviews</h2>
<svg class="reviews-next" width="16" height="16" viewBox="0 0 16 16"><circle cx="8" cy="8" r="8" fill="#ccc"/><polygon points="6,4.5 11,8 6,11.5" fill="#fff"/></svg>
<div class="review-card">
  <blockquote>“ Phasellus hendrerit nibh nisl, quis fringilla augue iaculis quis. Maecenas nisi felis, condimen tum quis congue quis, iaculis eget felis. ”</blockquote>
  <cite>Client name, City</cite>
</div>

<aside class="sidebar">
  <h2>Latest Release</h2>
</aside>
<div class="book latest" style="left:845px">
  <div class="cover" role="img" aria-label="Book cover artwork for The Second Tide: a ringed planet on a red and black ground"></div>
  <h3>The Second Tide</h3>
  <p style="top:42px">Lumen Version<br>Hard Copy</p>
</div>
<div class="book first" style="left:845px">
  <div class="cover" role="img" aria-label="Book cover artwork for the first novel: a grey moon over a dark sky"></div>
  <h3>Where to Buy the First Chronicle</h3>
  <p style="top:86px">Lumen Version<br>from Riverstall</p>
</div>

<footer class="site-footer">
  <div class="footer-links">
    <a>Home</a><span class="sep">|</span><a>Reviews</a><span class="sep">|</span><a>About</a><span class="sep">|</span><a>Blog</a><span class="sep">|</span><a>Contact</a><span class="sep">|</span><a>News</a><span class="sep">|</span><a>Links</a>
  </div>
  <div class="copyright">Copyright &copy; 2014 &nbsp;The Morrow Ledgers. &nbsp;All rights reserved.</div>
  <div class="footer-social" style="left:930px"></div>
  <div class="footer-social" style="left:963px"></div>
  <div class="footer-social" style="left:997px"></div>
  <svg class="footer-social" style="left:1030px" width="25" height="25" viewBox="0 0 25 25"><rect x="6" y="8" width="13" height="9" fill="none" stroke="#ddd" stroke-width="1.4"/><polyline points="6,8 12.5,13 19,8" fill="none" stroke="#ddd" stroke-width="1.4"/></svg>
</footer>

</body>
</html>
```